B2B Case Study Template Design (InDesign or Affinity Designer)

Hello,We are a company specializing in custom sanitary space fit-outs and Solid Surface manufacturing. We are looking for a talented layout designer to create a professional and modern "Case Study" template to showcase our projects.This template must strictly be designed using Adobe InDesign or Affinity Designer. We do not want Canva, Word, or PowerPoint files.Attached, there is a file you can reference named "Balu - Case Study.pdf". This is our previous layout.

Your mission is to recreate this case study using our new brand guidelines (which I will also provide) while using the exact same texts, photos, and sections (Key Data / "Données clés", Verlo's Role / "Le rôle d'Verlo", Verlo Products / "Produits Verlo").

Note: This project is the first of a series. We want to keep everything in the same project scope moving forward. If the work is satisfactory, we will hire you directly for upcoming print materials (flyer templates, catalogs, etc.).

---
2 Exemples of existing Case Studies : BALU and SOFT RIM
1 Full INDISIGN assembled file for DELORME project (you can work from there)
The logo (multi format)
And a zip file with the PATTERN, FONT and LOGO ALTERNATIVES (for graphic use only - on a photo, or else)

Target Market(s)

Building professionals, architects, specifiers, B2B companies, and contractors.

Industry/Entity Type

Architecture / Construction / B2B

Font styles to use
Sans Serif

Requirements
Must have
• The final source file must be delivered in Adobe InDesign (.indd/.idml) or Affinity Designer format. The design must be clean, structured, and highlight the architectural photography. Paragraph and character styles must be properly set up in the software so we can easily edit the text ourselves in the future. Strict integration of our new brand guidelines (colors, typography).
Nice to have
• A modular design: a layout that works perfectly for a 2-page (front/back) document, but can be easily expanded to 3 or 4 pages if a specific case study requires more content. Layout suggestions for recurring graphic elements (e.g., custom icons for key data, elegant frames for pull quotes).
Should not have
• Do NOT use Canva, Microsoft Word, or Photoshop for the layout. Avoid cluttered, overly colorful, or whimsical designs. We are looking for a premium, high-end, and serious aesthetic suited for the architectural field.

```html
<!DOCTYPE html>
<html lang="fr">
<head>
<meta charset="utf-8">
<title>Verlo – Étude de cas Projet Delorme</title>
<link href="https://fonts.googleapis.com/css2?family=Playfair+Display:wght@700&family=Libre+Caslon+Display&family=Poppins:wght@300;400;500;600;700&display=swap" rel="stylesheet">
<style>
:root{
  --backdrop:#a3a1a3;
  --paper:#f5f4f1;
  --slate:#7b8a96;
  --slate-light:#a3b0ba;
  --slate-pattern:#83929d;
  --charcoal:#2f2d2c;
  --ink:#2a2a2a;
  --muted:#6c7a85;
  --accent:#8a5a44;
  --beige:#efe7d6;
  --serif-bold:"Playfair Display",Georgia,serif;
  --serif:"Libre Caslon Display",Georgia,serif;
  --sans:"Poppins",Arial,sans-serif;
}
*{margin:0;padding:0;box-sizing:border-box}
html,body{width:1200px;height:3471px;overflow:hidden}
body{background:var(--backdrop);position:relative;font-family:var(--sans);color:var(--ink)}
.sheet{position:absolute;left:85px;width:1030px;height:729px;background:var(--paper);overflow:hidden}
.abs{position:absolute}
.photo{position:absolute}
.wordmark{position:absolute;font-family:var(--sans);font-weight:600;letter-spacing:.28em;line-height:1}

/* cover */
.cover{top:132px}
.cover .wordmark{left:640px;top:28px;font-size:38px;color:var(--ink)}
.cover .side-mark{left:24px;top:560px;font-size:30px;color:var(--ink);writing-mode:vertical-rl;transform:rotate(180deg);top:420px;left:40px}
.cover-photo{left:97px;top:84px;width:844px;height:512px;background:linear-gradient(180deg,#3e4447 0%,#6e7273 30%,#d7d6d2 45%,#8d8f8e 70%,#3a3c3d 100%)}
.cover-band{left:639px;top:371px;width:27px;height:358px;background:var(--slate)}
.cover-panel{left:666px;top:371px;width:364px;height:358px;background:var(--paper);padding:30px 0 0 24px}
.cover-title{font-family:var(--serif-bold);font-size:40px;line-height:1.08;color:var(--slate)}
.cover-sub{margin-top:48px;font-family:var(--serif);font-size:27px;line-height:1.2;text-transform:uppercase;color:var(--ink)}
.contact{left:112px;top:620px}
.contact h4{font-size:11px;font-weight:600;margin-bottom:10px}
.contact .col{position:absolute;top:24px;font-size:8.5px;line-height:1.6;color:#444;width:110px}
.contact .col b{display:block;font-weight:500;color:var(--slate);margin-bottom:4px}

/* spread 2 */
.spread2{top:971px}
.page-right{position:absolute;left:515px;top:0;width:515px;height:729px}
.s2-title{left:30px;top:30px;font-family:var(--serif);font-size:27px;line-height:1;color:var(--ink);width:470px}
.s2-title span{color:var(--slate)}
.s2-photo{left:0;top:98px;width:512px;height:272px;background:linear-gradient(180deg,#6b6a52 0%,#dedcd5 45%,#8a6446 70%,#5c5b4a 100%)}
.s2-intro{left:30px;top:380px;width:470px;font-size:8.5px;line-height:1.45;color:#333}
.s2-intro p{margin-bottom:5px}
.kd-head{font-size:12.5px;font-weight:700;color:var(--muted);letter-spacing:.02em}
.kd-list{margin-top:12px;font-size:8.2px;line-height:1.45;list-style:none}
.kd-list li{position:relative;padding-left:14px}
.kd-list li::before{content:"";position:absolute;left:2px;top:5px;width:4px;height:4px;border-radius:50%;background:var(--ink)}
.products-label{left:30px;top:571px;font-size:12.5px;font-weight:700;color:var(--muted)}
.product{position:absolute;top:570px;height:93px}
.product-cap{position:absolute;top:669px;font-size:10.5px;line-height:1.1;text-align:center;color:var(--ink)}
.s2-right{background:var(--slate);color:#fff}
.s2-rtitle{left:34px;top:36px;font-family:var(--serif);font-size:27px;color:var(--ink)}
.s2-rintro{left:34px;top:121px;width:440px;font-size:8.6px;line-height:1.9;color:#1f2326}
.s2-rintro p:first-child{font-size:10px;margin-bottom:4px}
.s2-rphoto{left:34px;top:218px;width:218px;height:368px;background:linear-gradient(180deg,#8a8c7a 0%,#dcdad4 50%,#8e6a4c 80%,#707162 100%)}
.s2-points{left:268px;top:219px;width:230px;color:#1f2326}
.s2-points h3{font-size:12.5px;font-weight:700;margin-bottom:12px}
.s2-points p{font-size:8.3px;line-height:1.4;margin-bottom:7px}
.s2-points h3.second{margin-top:16px}
.s2-pattern{left:0;top:620px;width:515px;height:109px;background:var(--slate-pattern)}

/* spread 3 */
.spread3{top:1810px}
.s3-photo{left:106px;top:67px;width:924px;height:597px;background:linear-gradient(180deg,#6f7170 0%,#b9b8b4 20%,#e8e7e3 45%,#c9c8c4 65%,#2e3031 100%)}
.quote-box{left:30px;top:0;width:259px;height:245px;background:var(--charcoal);padding:42px 0 0 32px}
.quote-mark{font-family:var(--serif-bold);font-size:70px;line-height:.6;color:var(--accent);height:36px}
.quote-big{margin-top:14px;font-family:var(--serif);font-size:26px;line-height:1.05;color:#fff}
.quote-big span{color:var(--slate-light)}
.quote-small{margin-top:28px;font-size:9.5px;line-height:1.2;color:#fff;width:200px}
.s3-mark{right:40px;top:670px;font-size:46px;color:var(--ink)}

/* spread 4 */
.spread4{top:2650px;background:var(--charcoal)}
.s4-right{background:var(--slate)}
.s4-title{left:30px;top:42px;font-family:var(--serif);font-size:23px;line-height:1.35;color:#fff}
.s4-title span{display:block;font-size:29px;color:var(--slate-light)}
.s4-sub{left:30px;top:104px;font-size:10.5px;color:#fff}
.s4-photo{left:124px;top:164px;width:155px;height:248px;background:linear-gradient(180deg,#7e806a 0%,#efeeea 50%,#7b5a40 85%,#55554a 100%)}
.s4-lead{left:299px;top:168px;width:170px;font-size:11.5px;font-weight:700;line-height:1.15;color:#fff}
.s4-lead p+p{margin-top:8px}
.s4-plans{left:30px;top:413px;width:314px;height:316px;background:var(--beige)}
.s4-depth{left:356px;top:376px;width:140px;color:#ddd}
.s4-depth h4{font-size:8.6px;font-weight:500;color:var(--slate-light);margin-bottom:10px}
.s4-depth li{font-size:8.2px;line-height:1.4;margin-left:10px;margin-bottom:4px}
.s4-mark{left:388px;top:640px;font-size:36px;color:#fff}
.s4-rtitle{left:66px;top:42px;font-family:var(--serif);font-size:23px;color:#fff}
.s4-rsub{left:66px;top:104px;font-size:10.5px;color:#fff}
.s4-rlead{left:66px;top:163px;width:400px;font-size:11px;font-weight:700;line-height:1.15;color:#fff}
.icon-item{position:absolute;top:240px;width:200px;color:#fff}
.icon-item .head{display:flex;gap:8px;align-items:flex-start}
.icon-item .head p{font-size:8.2px;line-height:1.25;font-weight:500}
.icon-item .body{margin-top:12px;font-size:8.2px;line-height:1.4;color:#eef1f3}
.s4-rphoto{left:66px;top:358px;width:384px;height:183px;background:linear-gradient(180deg,#71725f 0%,#d6d3cb 55%,#8d6a4c 100%)}
.s4-foot{left:66px;top:572px;width:420px;color:#fff}
.s4-foot .label{position:absolute;left:44px;top:0;width:74px;font-size:8.4px;font-weight:500;line-height:1.3;text-align:right}
.s4-foot .text{position:absolute;left:130px;top:0;width:282px;font-size:8.2px;line-height:1.4}
.s4-foot .text p{margin-bottom:6px}
</style>
</head>
<body>

<!-- Cover -->
<section class="sheet cover">
  <div class="wordmark">VERLO</div>
  <div class="photo cover-photo" role="img" aria-label="Photo d'un double plan vasque blanc avec miroir éclairé dans des sanitaires rénovés"></div>
  <div class="wordmark side-mark">VERLO</div>
  <div class="abs cover-band"></div>
  <div class="abs cover-panel">
    <h1 class="cover-title">PROJET<br>DELORME</h1>
    <p class="cover-sub">L’art de l’agilité :<br>rénovation<br>sanitaire<br>en site occupé</p>
  </div>
  <div class="abs contact">
    <h4>Prendre contact.</h4>
    <div class="col" style="left:0"><b>Adresse</b>Rue des Tilleuls, 43000 Valmont<br>France.</div>
    <div class="col" style="left:128px"><b>Site Web</b>www.verlo.fr<br>info@verlo.fr</div>
    <div class="col" style="left:238px"><b>Téléphone</b>+33 4 00 00 00 00</div>
  </div>
</section>

<!-- Spread 2 -->
<section class="sheet spread2">
  <h2 class="abs s2-title">Projet Delorme : <span>quand la performance s’adapte à la continuité de service</span></h2>
  <div class="photo s2-photo" role="img" aria-label="Photo d'un plan vasque blanc sur meuble bois dans des sanitaires d'open space"></div>
  <div class="abs s2-intro">
    <p>L’enjeu majeur du chantier Delorme résidait dans l’environnement immédiat : des open spaces occupés par des collaborateurs en plein travail.</p>
    <p>Ce projet exigeait donc une discrétion absolue et une rapidité d’exécution chirurgicale, dans le but de maintenir le confort des usagers pendant la transformation des espaces sanitaires.</p>
  </div>
  <div class="abs" style="left:63px;top:455px;width:160px">
    <h3 class="kd-head">DONNÉES CLÉ</h3>
    <ul class="kd-list">
      <li>Lieu : 12 Rue Delorme, Paris 17e (Immeuble bureaux Premium)</li>
      <li>Maître d’ouvrage : Banque Aurel</li>
      <li>Maître d’œuvre : Ostra Bâtiment</li>
      <li>Livraison : 2026</li>
    </ul>
  </div>
  <div class="abs" style="left:237px;top:455px;width:190px">
    <h3 class="kd-head">LE RÔLE D’Verlo</h3>
    <ul class="kd-list">
      <li>Conception de mobilier MERIS sur-mesure à profondeur variable</li>
      <li>Planification de pose par tranches</li>
      <li>Logistique de propreté «Zéro Poussière»</li>
      <li>Installation en mode «Discret»</li>
    </ul>
  </div>
  <div class="abs products-label">PRODUITS Verlo</div>
  <div class="product" style="left:158px;width:105px;background:linear-gradient(180deg,#f2f2f0,#dcdcda)" role="img" aria-label="Photo produit vasque blanche avec robinets"></div>
  <div class="product" style="left:263px;width:105px;background:linear-gradient(180deg,#c9c7c2,#e6e4df)" role="img" aria-label="Photo produit support de vasque sur-mesure"></div>
  <div class="product" style="left:368px;width:116px;background:linear-gradient(135deg,#e4e5e6,#c4c6c8)" role="img" aria-label="Photo produit miroir sur mesure"></div>
  <div class="product-cap" style="left:158px;width:105px">VASQUE ORLA<br>VB310</div>
  <div class="product-cap" style="left:263px;width:105px">Support MERIS<br>Sur-mesure</div>
  <div class="product-cap" style="left:368px;width:116px">miroir<br>sur mesure</div>

  <div class="page-right s2-right">
    <h2 class="abs s2-rtitle">UNE PROUESSE D’AGILITÉ :</h2>
    <div class="abs s2-rintro">
      <p>Maintenir le confort des usagers pendant la mutation des espaces.</p>
      <p>L’enjeu majeur du chantier Delorme résidait dans l’environnement immédiat :<br>des open spaces occupés par des collaborateurs en plein travail.<br>Ce projet « Delorme » exigeait donc une discrétion absolue<br>et une rapidité d’exécution chirurgicale.</p>
    </div>
    <div class="photo s2-rphoto" role="img" aria-label="Photo d'un lave-mains blanc sur meuble bois dans un sanitaire étroit"></div>
    <div class="abs s2-points">
      <h3>1. Mode «Discret» &amp; propreté :</h3>
      <p>Travailler dans le silence et sans dégagement de poussière était une condition non négociable.</p>
      <p>Verlo a mis en place un protocole spécifique pour garantir une propreté absolue des parties communes et des sanitaires, permettant aux occupants de continuer leurs activités sans nuisance.</p>
      <h3 class="second">2. Flux de travail «Chrono» :</h3>
      <p>Pour éviter la fermeture simultanée de tous les sanitaires de l’immeuble, Verlo a orchestré une pose par tranches successives.</p>
      <p>Ce phasage dynamique a permis de maintenir la continuité de service pour le client tout en assurant un temps de travaux record par étage.</p>
    </div>
    <div class="abs s2-pattern" role="img" aria-label="Bande de motif de marque répété"></div>
  </div>
</section>

<!-- Spread 3 -->
<section class="sheet spread3">
  <div class="photo s3-photo" role="img" aria-label="Photo d'un triple plan vasque blanc avec robinets muraux dans des sanitaires sombres"></div>
  <div class="abs quote-box">
    <div class="quote-mark">”</div>
    <p class="quote-big"><span>Add Big Text Her</span><br>Pull quotes Lorem<br>ipsuminate</p>
    <p class="quote-small">Odium, consulessi in defex mena, quaster urorum immordicerum hem avocaes notil</p>
  </div>
  <div class="wordmark s3-mark">VERLO</div>
</section>

<!-- Spread 4 -->
<section class="sheet spread4">
  <h2 class="abs s4-title">MOBILIER MERIS :<span>L’INTELLIGENCE DU SUR-MESURE</span></h2>
  <p class="abs s4-sub">S’adapter à l’existant sans compromis sur le design.</p>
  <div class="photo s4-photo" role="img" aria-label="Photo d'un lave-mains sur meuble bois avec sèche-mains mural"></div>
  <div class="abs s4-lead">
    <p>Le projet Delorme a nécessité une adaptation rare</p>
    <p>de notre gamme de supports de fixation.</p>
  </div>
  <div class="abs s4-plans" role="img" aria-label="Plans techniques cotés et vue 3D du meuble lave-mains"></div>
  <div class="abs s4-depth">
    <h4>Profondeurs atypiques :</h4>
    <ul>
      <li>Le bureau d’études Verlo a redessiné le mobilier MERIS pour répondre à des profondeurs de niches sortant des standards habituels, optimisant ainsi chaque centimètre carré d’espace.</li>
      <li>De plus, la redéfinition du support a permis l’ajout de rangements sous-jacents, permettant le stockage de matériel d’entretien, etc.</li>
    </ul>
  </div>
  <div class="wordmark s4-mark">VERLO</div>

  <div class="page-right s4-right">
    <h2 class="abs s4-rtitle">DE LA CONCEPTION À LA POSE :</h2>
    <p class="abs s4-rsub">Une responsabilité totale pour un résultat garanti.</p>
    <p class="abs s4-rlead">Au-delà de la technique, ce projet représente également comment la société Verlo prend la responsabilité du résultat final en assurant<br>elle-même la pose de ses produits.</p>
    <div class="icon-item" style="left:66px">
      <div class="head">
        <svg width="34" height="26" viewBox="0 0 34 26" fill="none" stroke="#fff" stroke-width="1.2"><rect x="14" y="3" width="12" height="14"/><path d="M2 21h28M6 21V5h4v16M10 12h4"/><circle cx="7" cy="23" r="2"/><circle cx="24" cy="23" r="2"/></svg>
        <p>Manutention maîtrisée :<br>Une logistique invisible<br>en milieu occupé</p>
      </div>
      <p class="body">Livraison et acheminement en milieu occupé sans perturber les flux de l’immeuble, en dehors des pics d’affluence.</p>
    </div>
    <div class="icon-item" style="left:250px;width:205px">
      <div class="head">
        <svg width="46" height="26" viewBox="0 0 46 26" fill="none" stroke="#fff" stroke-width="1.2"><rect x="2" y="8" width="18" height="12"/><path d="M20 12h8l5 5v3H20"/><circle cx="8" cy="22" r="2.5"/><circle cx="27" cy="22" r="2.5"/><rect x="32" y="3" width="12" height="12"/></svg>
        <p>Précision de pose :<br>L’ingénierie face aux<br>contraintes de la rénovation</p>
      </div>
      <p class="body">Ajustement des structures sur-mesure sur des supports existants parfois irréguliers &amp; redimensionnement du mobilier Meris pour s’adapter aux contraintes présentes et modification de sa profondeur.</p>
    </div>
    <div class="photo s4-rphoto" role="img" aria-label="Photo de chantier avec cotes de mesure annotées sur le mur du sanitaire"></div>
    <div class="abs s4-foot">
      <svg class="abs" style="left:0;top:2px" width="36" height="36" viewBox="0 0 36 36" fill="none" stroke="#fff" stroke-width="1.3"><path d="M6 30L22 14M20 8a6 6 0 0 0 8 8l-3-3 2-2 3 3a6 6 0 0 0-8-8zM6 6l4 0 14 14 4 8-8-4L6 10z"/></svg>
      <p class="label">Engagement rapidité : un phasage précis pour la continuité de service</p>
      <div class="text">
        <p>L’installation a été orchestrée par tranches successives pour éviter la fermeture simultanée de tous les points d’eau et maintenir le confort des collaborateurs.</p>
        <p>Grâce à un pré-montage maximal dans notre atelier de Haute-Loire, le temps d’intervention physique sur le site de Delorme a été réduit au strict minimum.</p>
        <p>Chaque journée s’est conclue par un nettoyage rigoureux «fin de poste», permettant une restitution immédiate des locaux, sans poussière ni nuisances.</p>
      </div>
    </div>
  </div>
</section>

</body>
</html>
```